Brin-well Tide Port Custom Brokers Limited

Name: Loranda Pascoe
Title: Customs Broker
Address: Shop 9 Fernvale Commercial Complex
227-229 Marrow Lane
Kingston 8
Telephone: (876)
Email: tideportbrin@quillmail.example

```html
<!DOCTYPE html>
<html lang="en">
<head>
<meta charset="utf-8">
<title>Brin-well Tide Port Custom Brokers Limited – Business Card</title>
<link rel="stylesheet" href="https://fonts.googleapis.com/css2?family=Lato:wght@400;700;900&display=swap">
<style>
  :root {
    --navy: #14294d;
    --gold: #e9a928;
    --white: #ffffff;
    --ink-soft: #5a5f68;
    --backdrop: #e6e4e1;
  }
  * { box-sizing: border-box; margin: 0; padding: 0; }
  html, body { width: 1200px; height: 847px; overflow: hidden; }
  body {
    background: var(--backdrop);
    font-family: "Lato", Arial, sans-serif;
    display: flex;
    align-items: center;
    justify-content: center;
    gap: 40px;
  }
  .card {
    width: 540px;
    height: 309px;
    position: relative;
    border-bottom: 4px solid var(--gold);
    border-right: 4px solid var(--gold);
    box-shadow: 0 6px 18px rgba(0,0,0,.18);
  }

  /* Front */
  .card--front {
    background: var(--navy);
    display: flex;
    align-items: center;
    justify-content: center;
  }
  .brand {
    display: flex;
    align-items: center;
    gap: 14px;
    font-weight: 900;
    line-height: 1.05;
  }
  .brand__dot {
    width: 22px; height: 22px; border-radius: 50%;
    background: var(--gold);
    flex: none;
  }
  .brand__name { display: flex; flex-direction: column; }
  .brand__main { font-size: 30px; letter-spacing: .5px; text-transform: uppercase; }
  .brand__sub { font-size: 17px; letter-spacing: 3px; margin-top: 4px; }
  .card--front .brand { color: var(--white); }

  /* Back */
  .card--back { background: var(--white); border-left: 1px solid #eee; border-top: 1px solid #eee; }
  .card--back .brand { position: absolute; top: 42px; right: 30px; color: var(--navy); }
  .card--back .brand__main { font-size: 19px; }
  .card--back .brand__sub { font-size: 11px; letter-spacing: 2px; }
  .card--back .brand__dot { width: 16px; height: 16px; }

  .person { position: absolute; left: 34px; top: 44px; }
  .person__name { font-size: 25px; font-weight: 900; color: var(--navy); }
  .person__name span { color: var(--gold); }
  .person__title { font-size: 14px; color: var(--ink-soft); margin-top: 3px; }

  .contacts { position: absolute; left: 34px; top: 116px; list-style: none; }
  .contacts li {
    display: flex; align-items: center; gap: 10px;
    font-size: 14px; color: var(--ink-soft); height: 22px;
  }
  .contacts svg { width: 13px; height: 13px; flex: none; }

  .divider {
    position: absolute; left: 34px; right: 30px; top: 200px;
    height: 2px; background: var(--gold);
  }
  .address {
    position: absolute; right: 30px; top: 214px;
    text-align: right; font-size: 15px; line-height: 1.35; color: var(--ink-soft);
  }
</style>
</head>
<body>

<section class="card card--front" aria-label="Card front">
  <div class="brand">
    <span class="brand__dot"></span>
    <div class="brand__name">
      <span class="brand__main">Brin-well Tide Port</span>
      <span class="brand__sub">Custom Brokers Ltd.</span>
    </div>
  </div>
</section>

<section class="card card--back" aria-label="Card back">
  <div class="person">
    <h1 class="person__name">Loranda <span>Pascoe</span></h1>
    <p class="person__title">Customs Broker</p>
  </div>

  <ul class="contacts">
    <li>
      <svg viewBox="0 0 16 16" aria-hidden="true"><path fill="var(--gold)" d="M3.6 1.2l2.3 2.4-1.3 1.8c.9 2 2.6 3.7 4.6 4.6l1.8-1.3 2.4 2.3-1.5 2.6C6.7 13.2 2.8 9.3 1 4.1z"/></svg>
      (876) 555 0142
    </li>
    <li>
      <svg viewBox="0 0 16 16" aria-hidden="true"><rect x="1" y="3" width="14" height="10" rx="1" fill="var(--gold)"/><path d="M1.5 3.8L8 9l6.5-5.2" stroke="#fff" stroke-width="1.3" fill="none"/></svg>
      tideportbrin@quillmail.example
    </li>
    <li>
      <svg viewBox="0 0 16 16" aria-hidden="true"><circle cx="8" cy="8" r="7" fill="var(--gold)"/><path d="M1 8h14M8 1v14M3 4.5h10M3 11.5h10" stroke="#fff" stroke-width=".9" fill="none"/></svg>
      www.tideportbrin.example
    </li>
  </ul>

  <div class="brand">
    <span class="brand__dot"></span>
    <div class="brand__name">
      <span class="brand__main">Brin-well Tide Port</span>
      <span class="brand__sub">Custom Brokers Ltd.</span>
    </div>
  </div>

  <div class="divider"></div>

  <address class="address" style="font-style:normal">
    Shop 9 Fernvale Commercial Complex<br>
    227-229 Marrow Lane<br>
    Kingston 8
  </address>
</section>

</body>
</html>
```